11"x17" Poster for a Treasure Hunt

Summary:
This project is for a poster that will be used to promote a community treasure hunt for kids aged 9-14. This will be the 12th year we have run the treasure hunt. See the files for previous posters we have used (from PixelGuildry).

***Please thoroughly read below before embarking on this project.

We loved everything about the 2012 design, particularly how all of the elements seem to belong exactly where they are on the poster. Previous years designs just had text blocks thrown on top of a background image which doesn't make a for a good poster; if within a few seconds you don’t have an idea about what even the poster is promoting, and if you can’t read every part of the poster from 6 feet away, the poster isn't working.

Please make the Millbrook Quest Seekers logo a featured part of the design. See the 2012 poster winner where the logo was right at the top and very prominent.

Style: Scary, but remember the event is for children 9-14years old. The title of the hunt this year is “1848 : The Dread of Crag Morrow". The theme this year will be the gold rush of 1848 in California, USA and the central villain a scary miner.

We want the miner to look scary with the following elements:
A big miners hat
A miners pic in one hand
A lantern with a candle in the other hand
A long beard and connecting mustache
A scar on one side of his face
Traditional miner overalls
*Attached is a picture of a miner I found on a google search. Use that type of look as a starting point.

Remember, we want scary, but NOT gross and gruesome as this is for kids 9-14. Some of the poster submissions from previous years were way too gruesome with blood and gore. Do keep in mind this event is for children. For good examples, see "MBQS 2012 Winner" below (our favorite to date).

Must have the logos of Tim Fawkner, Ridgeway Orthodontics, and Millbrook Quest Seekers.

Target Market(s)

Kids 9-14 years old

Industry/Entity Type

Community

Requirements
Must have
• Must have the following texts:
• 1848: The Dread of Crag Morrow
• October 14th, 2017
• Be the first team to unravel the mystery behind the legend of Crag Morrow and you will find a FANTASTIC TREASURE!
• Youth Ages 9-14 are eligible to participate
• Team applications open September 1st and are due ASAP.
• Space is limited to the first 50 teams
• Presented by Tim Fawkner of Hearth Propertiez and Dr. Neil Orsk of Ridgeway Orthodontics
• WWW.MILLBROOKQUESTSEEKERS.EXAMPLE
• **Must have Logos for Tim Fawkner, Ridgeway Orthodontics, and Millbrook Quest Seekers
Should not have
• No gory bloody pictures

```html
<!DOCTYPE html>
<html lang="en">
<head>
<meta charset="utf-8">
<title>1848 : The Dread of Crag Morrow – Millbrook Quest Seekers</title>
<link rel="stylesheet" href="https://fonts.googleapis.com/css2?family=Bangers&family=Creepster&display=swap">
<style>
  :root {
    --page-bg: #e6e6e6;
    --night-deep: #0f2a33;
    --night-teal: #24534d;
    --moon: #cdf3d2;
    --dusk: #3b3626;
    --ember: #9a3c14;
    --ember-hot: #d2561a;
    --title-yellow: #f7c51e;
    --ink-black: #0b0b0b;
    --treasure-red: #e2241b;
    --white: #ffffff;
  }
  * { margin: 0; padding: 0; box-sizing: border-box; }
  html, body {
    width: 1000px; height: 1200px; overflow: hidden;
    background: var(--page-bg);
  }
  .poster {
    position: absolute; left: 60px; top: 11px;
    width: 880px; height: 1178px; overflow: hidden;
    background: var(--night-deep);
    font-family: "Bangers", "Impact", sans-serif;
  }
  .scene {
    position: absolute; inset: 0;
    background:
      radial-gradient(circle at 63% 8%, var(--moon) 0, #7fd6a4 9%, rgba(60,140,110,.55) 18%, rgba(30,80,80,0) 32%),
      linear-gradient(180deg, var(--night-deep) 0%, var(--night-teal) 30%, var(--dusk) 55%, var(--ember) 80%, var(--ember-hot) 100%);
  }
  .miner-figure {
    position: absolute; left: 430px; top: 470px;
    width: 450px; height: 700px;
    background:
      radial-gradient(circle at 78% 62%, rgba(255,190,70,.85) 0, rgba(230,120,30,.5) 12%, rgba(0,0,0,0) 26%),
      radial-gradient(ellipse at 45% 45%, #7a3c1a 0, #4a2412 45%, rgba(40,20,10,0) 75%);
  }
  .brand {
    position: absolute; top: 78px; left: 0; width: 100%;
    display: flex; justify-content: center; align-items: center; gap: 12px;
    padding-left: 90px;
    color: var(--white); font-size: 40px; letter-spacing: 2px;
  }
  .brand-dot { width: 22px; height: 22px; border-radius: 50%; background: var(--white); }
  .title {
    position: absolute; left: 100px; top: 160px;
    font-family: "Creepster", "Impact", cursive;
    font-weight: 400;
    color: var(--title-yellow);
    text-shadow: 5px 6px 0 var(--ink-black);
    line-height: .95;
  }
  .title-top { display: block; font-size: 88px; }
  .title-name { display: block; font-size: 98px; margin-left: 10px; }
  .event-date {
    position: absolute; left: 80px; top: 395px; width: 290px;
    text-align: center; color: var(--title-yellow);
    font-size: 50px; line-height: 1.02;
    text-shadow: 3px 3px 0 var(--ink-black);
  }
  .challenge {
    position: absolute; left: 75px; top: 565px; width: 360px;
    color: var(--white); font-size: 24px; line-height: 1.05;
    text-shadow: 2px 2px 0 var(--ink-black);
  }
  .treasure {
    position: absolute; left: 78px; top: 672px;
    color: var(--treasure-red); font-size: 72px; line-height: .95;
    text-shadow: 3px 3px 0 var(--ink-black);
  }
  .entry-info {
    position: absolute; left: 75px; top: 835px; width: 380px;
    list-style: none;
    color: var(--title-yellow); font-size: 21px; line-height: 1.15;
    letter-spacing: .5px;
    text-shadow: 2px 2px 0 var(--ink-black);
  }
  .entry-info li + li { margin-top: 4px; }
  .presenters {
    position: absolute; left: 200px; top: 1058px; width: 500px;
    text-align: center; color: var(--white); font-size: 19px; line-height: 1.15;
    letter-spacing: .5px;
  }
  .website {
    position: absolute; left: 160px; top: 1108px; width: 580px;
    text-align: center; color: var(--white); font-size: 30px; letter-spacing: 1px;
  }
  .sponsor {
    position: absolute; display: flex; align-items: center; gap: 8px;
    color: var(--white); font-size: 20px; line-height: 1.05;
  }
  .sponsor-fawkner { left: 44px; top: 1090px; width: 150px; }
  .sponsor-ridgeway { left: 712px; top: 1080px; width: 150px; }
  .mark-square { flex: none; width: 22px; height: 22px; background: var(--white); }
  .mark-circle { flex: none; width: 22px; height: 22px; border-radius: 50%; background: var(--white); }
</style>
</head>
<body>
  <main class="poster">
    <div class="scene" role="img" aria-label="Night graveyard scene under a glowing green full moon with storm clouds, a crow on a bare branch and gravestones glowing orange below"></div>
    <div class="miner-figure" role="img" aria-label="Hooded bearded miner seen from behind, holding a lit candle lantern"></div>

    <header class="brand">
      <span class="brand-dot"></span>
      <span class="brand-name">Millbrook Quest Seekers</span>
    </header>

    <h1 class="title">
      <span class="title-top">1848 : The Dread</span>
      <span class="title-name">of Crag Morrow</span>
    </h1>

    <p class="event-date">October<br>14th, 2017</p>

    <p class="challenge">
      Be the first team to unravel<br>
      the mystery behind the legend<br>
      of Crag Morrow and you will find a
    </p>

    <p class="treasure">Fantastic<br>Treasure!</p>

    <ul class="entry-info">
      <li>Youth ages 9-14 are eligible to participate</li>
      <li>Team applications open September 1st<br>and are due ASAP.</li>
      <li>Space is limited to the first 50 teams</li>
    </ul>

    <div class="sponsor sponsor-fawkner">
      <span class="mark-square"></span>
      <span>Tim Fawkner</span>
    </div>

    <p class="presenters">
      Presented by Tim Fawkner of Hearth Propertiez and Dr. Neil Orsk<br>
      of Ridgeway Orthodontics
    </p>
    <p class="website">WWW.MILLBROOKQUESTSEEKERS.EXAMPLE</p>

    <div class="sponsor sponsor-ridgeway">
      <span class="mark-circle"></span>
      <span>Ridgeway<br>Orthodontics</span>
    </div>
  </main>
</body>
</html>
```